North American Image Consultant needs a process design and a method design

I am an Image/style consultant who works with business professionals in the Toronto area. My product name is called " R.E.S.K.A." I help people understand how your " Position, Industry, Volume, effects their Outcome and Time. I help people create a professional appearance in a business casual/digital world, from head to toe. I work with them through all 4 seasons, to achieve consistency and confidence to help them look and feel amazing, inside and out.. easily and effortlessly. My main colour is aqua blue, I don't want any neon or primary colours. I would like it to appeal to both men and women ( but mostly women)
The final design should be an easy to follow path to success with an understanding of what R.E.S.K.A will do for them.

Target Market(s)

mid level executive business professionals 38-58 yrs old they want to look and feel amazing inside and out. They want to up their game, get the promotion, nail the interview , and feel they're relevant and taken seriously in a leadership way.

Font styles to use
Serif

Colors
b7a5cd
886aae
85cae6
33a6d7
33b8a4
f04a50
00a990
e34297
85acd3

Requirements
Must have
• A classy, casual feel. A positive feel good feeling
Nice to have
• A 3 colour balance ( Not black based)
Should not have
• Too many squares
too many squiggly lines.
Not too masculine/feminine
too childish/youthful
Not office focused or bank focused

```html
<!DOCTYPE html>
<html lang="en">
<head>
<meta charset="utf-8">
<title>R.E.S.K.A. – Method</title>
<link href="https://fonts.googleapis.com/css2?family=Gelasio:wght@400;700&display=swap" rel="stylesheet">
<style>
  :root {
    --lavender: #b7a5cd;
    --violet: #886aae;
    --sky: #85cae6;
    --ocean: #33a6d7;
    --teal: #33b8a4;
    --ink: #111111;
    --muted: #7d7d80;
    --rule: #a7a7a9;
    --paper: #ffffff;
  }
  html, body {
    margin: 0;
    padding: 0;
    overflow: hidden;
    background: var(--paper);
  }
  .canvas {
    position: relative;
    width: 1200px;
    height: 675px;
    overflow: hidden;
    background: var(--paper);
    font-family: "Gelasio", Georgia, serif;
    color: var(--ink);
  }
  .artwork {
    position: absolute;
    inset: 0;
    width: 1200px;
    height: 675px;
  }
  .brand {
    position: absolute;
    left: 96px;
    top: 52px;
    margin: 0;
    font-size: 23.5px;
    line-height: 28px;
    font-weight: 700;
    letter-spacing: 0.3px;
  }
  .tagline {
    position: absolute;
    right: 84px;
    top: 53px;
    margin: 0;
    font-size: 20.5px;
    line-height: 28px;
    font-weight: 400;
    color: var(--muted);
  }
  .step {
    position: absolute;
  }
  .step--right { text-align: left; }
  .step--left { text-align: right; }
  .step__title {
    margin: 0;
    font-size: 21.5px;
    line-height: 26px;
    font-weight: 700;
  }
  .step__text {
    margin: 2px 0 0;
    font-size: 15px;
    line-height: 19px;
    font-weight: 400;
  }
  .step--position { left: 919px; top: 171px; }
  .step--industry { left: 970px; top: 341px; }
  .step--volume { left: 920px; top: 499px; }
  .step--time { right: 941px; top: 231px; }
  .step--outcome { right: 940px; top: 408px; }
</style>
</head>
<body>
<div class="canvas">
  <svg class="artwork" viewBox="0 0 2560 1440" aria-hidden="true">
    <defs>
      <clipPath id="ring-clip">
        <circle cx="1289" cy="744" r="385"/>
      </clipPath>
      <mask id="under-teal">
        <rect x="0" y="0" width="2560" height="1440" fill="#fff"/>
        <circle cx="1287" cy="612" r="257" fill="#000"/>
      </mask>
    </defs>

    <!-- header rule -->
    <rect x="204" y="170" width="2177" height="7" fill="var(--rule)"/>

    <!-- swirl -->
    <g class="swirl" clip-path="url(#ring-clip)" stroke="#fff" stroke-width="6">
      <circle cx="1163" cy="705" r="253" fill="var(--lavender)"/>
      <circle cx="1287" cy="612" r="253" fill="var(--teal)"/>
      <circle cx="1415" cy="705" r="253" fill="var(--sky)"/>
      <circle cx="1370" cy="853" r="253" fill="var(--ocean)"/>
      <circle cx="1213" cy="852" r="253" fill="var(--violet)"/>
      <circle cx="1163" cy="705" r="253" fill="var(--lavender)" mask="url(#under-teal)"/>
    </g>
    <circle cx="1288" cy="745" r="118" fill="var(--paper)"/>

    <!-- icons -->
    <g class="icons" fill="none" stroke="#fff" stroke-width="5" stroke-linecap="round" stroke-linejoin="round">
      <!-- hierarchy -->
      <g class="icon-hierarchy">
        <circle cx="1162" cy="443" r="11"/>
        <path d="M1146 470 q16 -16 32 0 v6 h-32 z"/>
        <path d="M1162 476 v14 M1128 490 h68 M1128 490 v10 M1162 490 v10 M1196 490 v10"/>
        <circle cx="1128" cy="508" r="8"/>
        <circle cx="1162" cy="508" r="8"/>
        <circle cx="1196" cy="508" r="8"/>
        <path d="M1117 527 q11 -12 22 0 M1151 527 q11 -12 22 0 M1185 527 q11 -12 22 0"/>
      </g>
      <!-- network -->
      <g class="icon-network">
        <circle cx="1452" cy="516" r="20"/>
        <circle cx="1420" cy="562" r="15"/>
        <circle cx="1480" cy="566" r="18"/>
        <path d="M1440 532 l-12 16 M1462 534 l10 14"/>
        <path d="M1432 506 l-20 -8 M1472 512 h20 M1472 522 l16 4"/>
        <circle cx="1408" cy="496" r="4"/>
        <circle cx="1496" cy="496" r="4"/>
        <circle cx="1492" cy="528" r="6"/>
        <path d="M1420 577 v6 h16"/>
        <circle cx="1440" cy="583" r="4"/>
      </g>
      <!-- megaphone -->
      <g class="icon-megaphone">
        <path d="M1510 850 l46 -36 l16 50 l-54 -2 z"/>
        <path d="M1510 850 l-12 6 l8 22 l12 -4"/>
        <path d="M1520 872 l18 22 l8 -6 l-12 -20"/>
        <path d="M1558 830 q14 -6 18 10"/>
        <path d="M1556 808 q24 -4 26 24"/>
      </g>
      <!-- stopwatch -->
      <g class="icon-stopwatch">
        <circle cx="1010" cy="796" r="40"/>
        <circle cx="1010" cy="796" r="30"/>
        <path d="M1000 746 h20 M1010 746 v10 M1038 764 l10 -10 l6 6 l-10 10"/>
        <path d="M1010 796 l14 -14"/>
        <circle cx="1010" cy="796" r="4"/>
        <path d="M1010 770 v4 M1010 818 v4 M984 796 h4 M1032 796 h4"/>
      </g>
      <!-- trophy -->
      <g class="icon-trophy">
        <path d="M1202 992 h56 v22 a28 28 0 0 1 -56 0 z"/>
        <path d="M1202 996 h-12 v8 a18 18 0 0 0 14 18 M1258 996 h12 v8 a18 18 0 0 1 -14 18"/>
        <circle cx="1230" cy="1013" r="14"/>
        <path d="M1230 1005 l3 6 l6 1 l-4 4 l1 6 l-6 -3 l-6 3 l1 -6 l-4 -4 l6 -1 z" stroke-width="3"/>
        <path d="M1230 1042 v20 M1216 1062 h28 M1208 1074 h44 M1216 1062 v12 M1244 1062 v12"/>
      </g>
    </g>

    <!-- connectors -->
    <g class="connectors" stroke-width="6">
      <g class="connector connector--teal" fill="var(--teal)" stroke="var(--teal)">
        <line x1="1692" y1="420" x2="1886" y2="420"/>
        <circle cx="1692" cy="420" r="15" stroke="none"/>
        <circle cx="1886" cy="420" r="13" stroke="none"/>
      </g>
      <g class="connector connector--sky" fill="var(--sky)" stroke="var(--sky)">
        <line x1="1804" y1="779" x2="1997" y2="779"/>
        <circle cx="1804" cy="779" r="15" stroke="none"/>
        <circle cx="1997" cy="779" r="13" stroke="none"/>
      </g>
      <g class="connector connector--ocean" fill="var(--ocean)" stroke="var(--ocean)">
        <line x1="1692" y1="1117" x2="1886" y2="1117"/>
        <circle cx="1692" cy="1117" r="15" stroke="none"/>
        <circle cx="1886" cy="1117" r="13" stroke="none"/>
      </g>
      <g class="connector connector--lavender" fill="var(--lavender)" stroke="var(--lavender)">
        <line x1="628" y1="548" x2="838" y2="548"/>
        <circle cx="628" cy="548" r="13" stroke="none"/>
        <circle cx="838" cy="548" r="15" stroke="none"/>
      </g>
      <g class="connector connector--violet" fill="var(--violet)" stroke="var(--violet)">
        <line x1="628" y1="923" x2="838" y2="923"/>
        <circle cx="628" cy="923" r="13" stroke="none"/>
        <circle cx="838" cy="923" r="15" stroke="none"/>
      </g>
    </g>
  </svg>

  <h1 class="brand">R.E.S.K.A.</h1>
  <p class="tagline">Maintaining a professional appearance in a business casual world</p>

  <div class="step step--right step--position">
    <h2 class="step__title">P - Position</h2>
    <p class="step__text">Level of authority</p>
  </div>
  <div class="step step--right step--industry">
    <h2 class="step__title">I - Industry</h2>
    <p class="step__text">Influence of environment</p>
  </div>
  <div class="step step--right step--volume">
    <h2 class="step__title">V - Volume</h2>
    <p class="step__text">The ‘Sound’ of your presence<br>when you walk into a room</p>
  </div>
  <div class="step step--left step--time">
    <h2 class="step__title">T - Time</h2>
    <p class="step__text">Save more, spend less</p>
  </div>
  <div class="step step--left step--outcome">
    <h2 class="step__title">O - Outcome</h2>
    <p class="step__text">Achieve consistent results</p>
  </div>
</div>
</body>
</html>
```